Natural Light/Organic/Documentary Photography Business

I like a simple, approachable, feminine, earthy/organic feel. Earth/neutral tones, nothing too loud or obnoxious. I like the watercolor look. I don't want anything too trendy or something I'll get tired of after a couple months. As far as colors, I am much more a fan of cream/taupe/blue/green...not a fan of pink or purple at all.

Target Market(s)

Weddings & Families

Industry/Entity Type

Wedding Photography

Contact Information for Business Card

website, email, phone number

Font styles to use
Other font styles liked:
• Horizontes, Gotham

Colors

Designer to choose colors to be used in the design.

Requirements
Must have
• Website: www.elspethmarlowe.com
• Phone: 412.638.9057
• Email: elspeth@elspethmarlowe.com
Nice to have
• I like the watercolor look but its not necessary. I like simple/earthy tones. Nothing too loud or distracting. Simple & feminine without being too girly. I like an approachable/soft feel.
• Instagram: www.instagram.com/elspethmarlowephotography/
Should not have
• NO loud colors or design or pattern. I do not want a photo of a camera or lens or anything cheesy like that.

```html
<!DOCTYPE html>
<html lang="en">
<head>
<meta charset="utf-8">
<title>Elspeth Marlowe Photography – Business Cards</title>
<link href="https://fonts.googleapis.com/css2?family=Lato:wght@300;400&display=swap" rel="stylesheet">
<style>
  :root {
    --backdrop: #8a8a8a;
    --card-white: #ffffff;
    --card-mist: #efefef;
    --ink: #3a3533;
    --taupe: #8b7e77;
    --rule: #8f8a86;
    --wash-green: #d6e2b8;
    --wash-fog: #dfe0de;
    --wash-peach: #ecc9b4;
    --wash-sage: #c9ddd0;
  }
  * { margin: 0; padding: 0; box-sizing: border-box; }
  html, body {
    width: 1200px; height: 1200px; overflow: hidden;
    background: var(--backdrop);
    font-family: "Lato", sans-serif;
  }
  .canvas { position: relative; width: 1200px; height: 1200px; }

  .card {
    position: absolute; top: 310px; height: 593px;
    box-shadow: 3px 4px 6px rgba(0,0,0,0.35);
    overflow: hidden;
  }
  .card--front { left: 235px; width: 363px; background: var(--card-white); }
  .card--back { left: 628px; width: 367px; background: var(--card-mist); }

  .artwork {
    position: absolute; left: 0; width: 100%;
  }
  .card--front .artwork {
    top: 0; height: 473px;
    background: linear-gradient(170deg, var(--wash-green) 0%, var(--wash-fog) 50%, var(--wash-peach) 100%);
  }
  .card--back .artwork {
    top: 467px; height: 126px;
    background: linear-gradient(100deg, var(--wash-green) 0%, var(--wash-fog) 55%, var(--wash-sage) 100%);
  }

  .brand {
    position: absolute; left: 0; width: 100%;
    text-align: center; color: var(--taupe); font-weight: 300;
  }
  .card--front .brand { top: 496px; }
  .card--back .brand { top: 116px; }
  .brand-name {
    font-size: 36px; line-height: 42px; letter-spacing: 1px;
  }
  .brand-tagline {
    margin-top: 2px;
    font-size: 8px; line-height: 10px; letter-spacing: 3.5px;
    text-transform: uppercase;
  }

  .divider {
    position: absolute; left: 112px; width: 150px; height: 1px;
    background: var(--rule);
  }
  .divider--top { top: 205px; }
  .divider--bottom { top: 335px; }

  .contact {
    position: absolute; top: 228px; left: 0; width: 100%;
    text-align: center; list-style: none;
    font-size: 19px; line-height: 24.5px; color: var(--ink);
  }
  .social {
    position: absolute; top: 366px; left: 0; width: 100%;
    text-align: center;
    font-size: 15px; color: var(--ink);
  }
</style>
</head>
<body>
  <main class="canvas">
    <section class="card card--front">
      <div class="artwork" role="img" aria-label="Abstract painted watercolour artwork in soft green, grey and peach tones"></div>
      <div class="brand">
        <p class="brand-name">Elspeth Marlowe</p>
        <p class="brand-tagline">Photography</p>
      </div>
    </section>

    <section class="card card--back">
      <div class="brand">
        <p class="brand-name">Elspeth Marlowe</p>
        <p class="brand-tagline">Photography</p>
      </div>
      <div class="divider divider--top"></div>
      <ul class="contact">
        <li>412.638.9057</li>
        <li>elspeth@elspethmarlowe.com</li>
        <li>www.elspethmarlowe.com</li>
      </ul>
      <div class="divider divider--bottom"></div>
      <p class="social">instagram.com/elspethmarlowephotography</p>
      <div class="artwork" role="img" aria-label="Band of abstract painted watercolour artwork in soft green, grey and sage tones"></div>
    </section>
  </main>
</body>
</html>
```